Meadowlark Learning Growth Partners (MLGP)

This is a professional business card. Logo and picture are a must on the front of the card. I am an educational consultant. I have been consulting for the past three years for a company. I am now opening my own company. My goal for my consulting company is to eventually consult all over America.

Target Market(s)

Educators, schools, professionals

Industry/Entity Type

Consulting

Contact Information for Business Card

Picture/logo on front, simple modern design

Font styles to use
Serif

Colors
85abd2
0355a3
3176b5
cedeed

Requirements
Must have
• picture, logo,
• Odessa Pruitt, Ed.S
• address 5073 Cormorant ridge Dr. Nashville, TN 37940
• Cell:616-555-0148
• Office: 629-555-0172
• www.Mlgpedu.example
• pruittodessa@mailbox.example

```html
<!DOCTYPE html>
<html lang="en">
<head>
<meta charset="utf-8">
<title>Meadowlark Learning Growth Partners – Business Card</title>
<link href="https://fonts.googleapis.com/css2?family=Montserrat:wght@800&family=Open+Sans:wght@400;700&display=swap" rel="stylesheet">
<style>
  :root {
    --stage: #1b1c1c;
    --navy: #1f3b73;
    --brand-blue: #3176b5;
    --deep-blue: #0355a3;
    --pale-blue: #cedeed;
    --mid-blue: #85abd2;
    --white: #ffffff;
  }
  * { box-sizing: border-box; margin: 0; padding: 0; }
  html, body { width: 1200px; height: 1000px; overflow: hidden; background: var(--stage); }
  body { position: relative; font-family: "Open Sans", Arial, sans-serif; }

  .card {
    position: absolute;
    left: 250px;
    width: 700px;
    height: 400px;
    border-radius: 22px;
    overflow: hidden;
  }
  .card--front { top: 60px; background: var(--pale-blue); }
  .card--back { top: 540px; background: var(--white); }

  /* Front */
  .front-shape { position: absolute; inset: 0; }
  .front-brand {
    position: absolute;
    left: 70px; top: 150px;
    display: flex; align-items: center; gap: 16px;
  }
  .brand-dot { width: 34px; height: 34px; border-radius: 50%; background: var(--navy); }
  .front-brand .brand-name {
    font-family: "Montserrat", Arial, sans-serif;
    font-weight: 800; font-size: 82px; letter-spacing: 4px;
    color: var(--navy); line-height: 1;
  }

  /* Back */
  .back-shape { position: absolute; inset: 0; }
  .back-brand {
    position: absolute; left: 48px; top: 34px;
    display: flex; align-items: center; gap: 14px;
  }
  .back-brand .brand-dot { width: 22px; height: 22px; }
  .back-brand .brand-name {
    font-family: "Montserrat", Arial, sans-serif;
    font-weight: 800; font-size: 28px; letter-spacing: 3px; color: var(--navy);
  }
  .brand-divider { width: 2px; height: 66px; background: var(--navy); }
  .brand-full {
    font-family: "Montserrat", Arial, sans-serif;
    font-weight: 800; font-size: 14px; line-height: 1.15; color: var(--navy);
  }
  .holder-name {
    position: absolute; left: 48px; top: 138px;
    font-weight: 700; font-size: 22px; color: var(--white);
  }
  .contact-list {
    position: absolute; left: 40px; top: 192px;
    list-style: none; color: var(--white); font-size: 17px;
  }
  .contact-list li { display: flex; align-items: center; gap: 10px; height: 28px; }
  .contact-list svg { width: 16px; height: 16px; flex: none; }
  .address {
    position: absolute; right: 44px; bottom: 34px;
    text-align: right; color: var(--white); font-size: 17px; line-height: 1.45;
  }
</style>
</head>
<body>

<section class="card card--front">
  <svg class="front-shape" viewBox="0 0 700 400" width="700" height="400">
    <defs>
      <linearGradient id="portraitTone" x1="0" y1="0" x2="0" y2="1">
        <stop offset="0" stop-color="#3f7dc4"/>
        <stop offset="0.55" stop-color="#2f66aa"/>
        <stop offset="1" stop-color="#1f2d4a"/>
      </linearGradient>
    </defs>
    <path d="M470,0 H700 V400 H430 C380,260 390,90 470,0 Z" fill="var(--white)"/>
    <path d="M505,0 H700 V400 H460 C412,260 420,90 505,0 Z" fill="url(#portraitTone)" role="img" aria-label="Portrait photo of Odessa Pruitt"/>
  </svg>
  <div class="front-brand">
    <span class="brand-dot"></span>
    <span class="brand-name">MLGP</span>
  </div>
</section>

<section class="card card--back">
  <svg class="back-shape" viewBox="0 0 700 400" width="700" height="400">
    <path d="M0,122 H300 L318,190 H700 V400 H0 Z" fill="var(--navy)"/>
    <line x1="318" y1="172" x2="700" y2="172" stroke="var(--navy)" stroke-width="2"/>
  </svg>
  <div class="back-brand">
    <span class="brand-dot"></span>
    <span class="brand-name">MLGP</span>
    <span class="brand-divider"></span>
    <span class="brand-full">Meadowlark<br>Learning<br>Growth<br>Partners</span>
  </div>
  <p class="holder-name">Odessa Pruitt, Ed.S</p>
  <ul class="contact-list">
    <li><svg viewBox="0 0 16 16"><rect x="4" y="1" width="8" height="14" rx="1.5" fill="none" stroke="currentColor" stroke-width="1.4"/></svg>616-555-0148</li>
    <li><svg viewBox="0 0 16 16"><path d="M4,1 L7,4 L5,6 C6,9 7,10 10,11 L12,9 L15,12 L13,15 C7,14 2,9 1,3 Z" fill="currentColor"/></svg>629-555-0172</li>
    <li><svg viewBox="0 0 16 16" fill="none" stroke="currentColor" stroke-width="1.2"><circle cx="8" cy="8" r="6.5"/><ellipse cx="8" cy="8" rx="3" ry="6.5"/><line x1="1.5" y1="8" x2="14.5" y2="8"/></svg>www.Mlgpedu.example</li>
    <li><svg viewBox="0 0 16 16"><rect x="1" y="3" width="14" height="10" fill="currentColor"/><path d="M1,3 L8,9 L15,3" fill="none" stroke="var(--navy)" stroke-width="1.3"/></svg>pruittodessa@mailbox.example</li>
  </ul>
  <p class="address">5073 Cormorant ridge<br>Dr. Nashville, TN 37940</p>
</section>

</body>
</html>
```